International travel site frontpage redesign

We sell tours to Scandinavia through our website www.brightfell-journeys.com. The website has become a bit old fashioned and we are in the process of making the website responsive. As you can see from the attached pictures the website will be wider with the responsive design, and our current design does not fit anymore.

Here is what we are looking for:
- A website that reflects a trustworthy and quality oriented company.
- Making the website more modern looking, but still recognisable (we want to keep the colours).
- keeping in mind that the age group of our customers are from 20-80 years old (most in their 60s).
- We want to remove the popular tours part and are instead looking to replace this with picture boxes the following subjects Scandinavia Specialist, Special Offers, Contact, Norway (or Norway Tours), Sweden (or Sweden Tours), Iceland (or Iceland Tours), Combination Tours. Possibly also Lapland, Winter, Northern Lights, Fjords and Capitals. Some of these categories can be smaller or perhaps half boxes; i.e. Winter and Northern lights in one. If we end up with four boxes per line perhaps we could add a social media box next to the three first ones.
- The above means that the left hand meny with Norway Tours, Sweden Tours etc will be redundant.
- we will add another line to the search Box (on the top): Destinations
- The top menu will have the same categories, but we need to add languages as the website will be in English and German.
- The footer must be changed
- We can take away the box to the right where it says "your window to booking the best of our world"

Target Market(s)

Travelling to Scandinavia is not low cost, so the website needs to appeal to those that can afford to travel to our destination.
The age group of our customers are from 20-80 years old (most in their 60s).

Industry/Entity Type

Travel

Number of Pages Required

1 page

Requirements
Should not have
• Flashy or cheap looking special offers...

```html
<!DOCTYPE html>
<html lang="en">
<head>
<meta charset="utf-8">
<title>Brightfell Journeys – Tours to Scandinavia</title>
<link href="https://fonts.googleapis.com/css2?family=Cinzel:wght@400&family=Bitter:wght@400;700&family=Open+Sans:wght@400;600;700&display=swap" rel="stylesheet">
<style>
:root{
  --red:#a80a0a;
  --red-dark:#8a0606;
  --green:#2f9a1f;
  --green-dark:#237a16;
  --ink:#333;
  --muted:#666;
  --line:#e2e2e2;
  --band:#ececec;
  --panel:#f3f3f3;
  --footer:#1f1f1f;
  --footer-text:#c9c9c9;
  --white:#fff;
}
*{margin:0;padding:0;box-sizing:border-box}
html,body{width:761px;height:1200px;overflow:hidden;background:var(--white)}
body{position:relative;font-family:"Open Sans",Arial,sans-serif;color:var(--ink);font-size:9px}
ul{list-style:none}

/* header */
.site-header{position:absolute;left:0;top:0;width:761px;height:59px;background:linear-gradient(#fff,#f4f4f4);border-bottom:2px solid var(--red)}
.brand{position:absolute;left:31px;top:23px;font-family:"Cinzel",serif;font-size:17px;color:#555;letter-spacing:.5px}
.lang{position:absolute;right:32px;top:12px;font-size:8px;color:#777}
.main-nav{position:absolute;right:16px;top:29px;display:flex}
.main-nav a{display:block;height:19px;line-height:19px;padding:0 11px;margin-left:6px;font-size:8.5px;color:#444;text-decoration:none;text-transform:uppercase}
.main-nav a.active{background:var(--red);color:var(--white);border-radius:2px}

/* hero */
.hero{position:absolute;left:0;top:59px;width:761px;height:305px}
.hero-photo{position:absolute;inset:0;background:linear-gradient(180deg,#8fb3c9 0%,#b7c9c6 35%,#c9c5a8 55%,#7f9b6a 75%,#4f6a3c 100%)}
.search-panel{position:absolute;left:0;top:0;width:209px;height:305px;background:rgba(60,64,66,.78);padding:28px 0 0 30px}
.search-panel h2{font-size:11px;font-weight:700;color:var(--white);text-transform:uppercase;margin-bottom:13px}
.field{position:relative;width:150px;height:23px;background:var(--white);margin-bottom:11.5px;font-size:8px;color:#666;line-height:23px;padding-left:8px}
.field svg{position:absolute;right:8px;top:9px}
.search-btn{display:block;width:150px;height:24px;margin-top:12px;background:linear-gradient(var(--red),var(--red-dark));color:var(--white);border:none;border-radius:3px;font:700 10px "Open Sans",sans-serif}

/* tagline */
.tagline{position:absolute;left:0;top:364px;width:761px;height:36px;background:var(--band);border-bottom:1px solid var(--line);font-family:"Bitter",serif;line-height:36px;padding-left:31px}
.tagline strong{font-size:17px;color:var(--red);font-weight:700;margin-right:10px}
.tagline span{font-size:14px;color:#333}
.slider-arrows{position:absolute;right:30px;top:10px;display:flex;gap:2px}
.slider-arrows i{display:block;width:15px;height:15px;background:#c9c9c9;position:relative}
.slider-arrows i+i{background:#999}
.slider-arrows svg{position:absolute;left:4px;top:4px}

/* destinations */
.destinations{position:absolute;left:34px;top:425px;display:flex;gap:13.5px}
.dest-card{position:relative;width:164px;height:111px;background:var(--white);padding:4px;box-shadow:0 0 4px rgba(0,0,0,.18)}
.dest-card .photo{width:100%;height:100%}
.dest-tag{position:absolute;left:-4px;top:11px;background:var(--red);color:var(--white);font-size:10px;font-weight:700;padding:3px 10px}
.dest-tag::after{content:"";position:absolute;left:0;bottom:-5px;border-top:5px solid #5e0404;border-left:4px solid transparent}

/* info band */
.info-band{position:absolute;left:0;top:564px;width:761px;height:117px;background:#eee}
.info-tiles{position:absolute;left:29px;top:22px;display:flex;gap:12px}
.info-tile{position:relative;width:167px;height:70px}
.info-tile .photo{width:100%;height:100%}
.info-tile span{position:absolute;left:0;bottom:0;width:100%;height:22px;background:rgba(40,40,40,.75);color:var(--white);font-size:10px;font-weight:700;line-height:22px;padding-left:10px;white-space:nowrap}
.info-buttons{position:absolute;left:564px;top:24px;width:167px}
.info-buttons a{display:block;height:28px;line-height:28px;text-align:center;color:var(--white);font-weight:700;font-size:10px;text-decoration:none;margin-bottom:12px;border-radius:2px}
.btn-protection{background:linear-gradient(var(--red),var(--red-dark))}
.btn-insurance{background:linear-gradient(#3aac27,var(--green-dark))}

/* offers */
.tabs{position:absolute;left:29px;top:712px;display:flex}
.tab{height:25px;line-height:25px;padding:0 26px 0 14px;font-size:10px;font-weight:700;color:var(--white);background:#888;margin-right:2px;clip-path:polygon(0 0,88% 0,100% 100%,0 100%)}
.tab.active{background:var(--red)}
.offers{position:absolute;left:29px;top:737px;width:701px;height:142px;background:var(--panel);border-top:2px solid var(--red)}
.offer-list{position:absolute;left:15px;top:14px;display:flex;gap:19px}
.offer-card{position:relative;width:154px;height:112px}
.offer-card .photo{width:100%;height:100%}
.offer-badge{position:absolute;right:0;top:0;width:28px;height:26px;background:var(--white);text-align:center;font-size:7px;line-height:8px;padding-top:5px;color:#333}
.offer-badge b{display:block;font-size:10px;color:var(--red)}
.offer-card span{position:absolute;left:0;bottom:8px;width:100%;height:24px;background:rgba(40,40,40,.72);color:var(--white);text-align:center;line-height:24px;font-size:9px;font-weight:700;white-space:nowrap}

/* footer */
.site-footer{position:absolute;left:0;top:907px;width:761px;height:293px;background:var(--footer);border-top:7px solid var(--red)}
.footer-col{position:absolute;top:21px}
.footer-col h3{font-size:9.5px;font-weight:700;color:var(--white);padding-bottom:8px;border-bottom:1px solid #333;margin-bottom:8px;width:120px}
.footer-col ul{margin-bottom:14px}
.footer-col li{font-size:7.6px;color:var(--footer-text);line-height:13.9px;padding-left:8px;position:relative;white-space:nowrap}
.footer-col li::before{content:"";position:absolute;left:0;top:6px;width:2px;height:2px;background:#999}
.footer-bottom{position:absolute;left:85px;top:250px;width:594px;border-top:1px solid #333;padding-top:14px;font-size:7.5px;color:var(--footer-text)}
.social{position:absolute;right:0;top:9px;display:flex;gap:5px}
.social i{display:block;width:16px;height:16px;border-radius:50%;background:#5a5a5a}
</style>
</head>
<body>

<header class="site-header">
  <div class="brand">BRIGHTFELL JOURNEYS</div>
  <div class="lang">EN / DE</div>
  <nav class="main-nav">
    <a class="active" href="#">Home</a><a href="#">Fjords</a><a href="#">Capitals</a><a href="#">Cruises</a><a href="#">Winter</a><a href="#">Pictures</a><a href="#">Contact</a>
  </nav>
</header>

<section class="hero">
  <div class="hero-photo" role="img" aria-label="Tropical beach with palm trees and a mossy driftwood trunk by the water"></div>
  <form class="search-panel">
    <h2>Search your tour</h2>
    <div class="field">All Destinations<svg width="6" height="4"><path d="M0 0l3 3 3-3" stroke="#555" fill="none"/></svg></div>
    <div class="field">All Tour Types<svg width="6" height="4"><path d="M0 0l3 3 3-3" stroke="#555" fill="none"/></svg></div>
    <div class="field">All Tour Selections<svg width="6" height="4"><path d="M0 0l3 3 3-3" stroke="#555" fill="none"/></svg></div>
    <div class="field">All Travel Periods<svg width="6" height="4"><path d="M0 0l3 3 3-3" stroke="#555" fill="none"/></svg></div>
    <div class="field">Free search</div>
    <button class="search-btn" type="button">Search</button>
  </form>
</section>

<div class="tagline">
  <strong>Breathtaking Adventure</strong><span>Enjoy Whitewater Refting During an Activity Tour</span>
  <div class="slider-arrows">
    <i><svg width="7" height="7"><path d="M5 0L1 3.5 5 7" stroke="#fff" fill="none"/></svg></i>
    <i><svg width="7" height="7"><path d="M2 0l4 3.5L2 7" stroke="#fff" fill="none"/></svg></i>
  </div>
</div>

<section class="destinations">
  <div class="dest-card"><div class="photo" role="img" aria-label="Tall iron tower against a sunset sky" style="background:linear-gradient(#9fb3c6,#d7b98d 60%,#5b6a43)"></div><span class="dest-tag">Norway</span></div>
  <div class="dest-card"><div class="photo" role="img" aria-label="Red rock mountain in a desert under blue sky" style="background:linear-gradient(#5d8fc9,#b4c9de 40%,#b5542a 60%,#6e5a2e)"></div><span class="dest-tag">Sweden</span></div>
  <div class="dest-card"><div class="photo" role="img" aria-label="Canal city at dusk with a gondola on the water" style="background:linear-gradient(#c98a6a,#e3a66e 45%,#6d4a55 70%,#3d3447)"></div><span class="dest-tag">Iceland</span></div>
  <div class="dest-card"><div class="photo" role="img" aria-label="Old town skyline on the waterfront at evening" style="background:linear-gradient(#7da0c9,#a9b8cf 45%,#b8825a 65%,#3f4e6a)"></div><span class="dest-tag">Combination</span></div>
</section>

<section class="info-band">
  <div class="info-tiles">
    <div class="info-tile"><div class="photo" role="img" aria-label="Stone bridge over a city canal" style="background:linear-gradient(#8fb3d9,#c9b49a 55%,#7d6a55)"></div><span>Scandinavian Specialist</span></div>
    <div class="info-tile"><div class="photo" role="img" aria-label="Traveller sitting on a rock above a misty valley" style="background:linear-gradient(#e6e0cf,#c9b89c 55%,#8a6f54)"></div><span>Travel Experiences</span></div>
    <div class="info-tile"><div class="photo" role="img" aria-label="Customer service team" style="background:linear-gradient(#d8dde2,#b9aea3 60%,#6c6b70)"></div><span>Customer Services (FAQ)</span></div>
  </div>
  <div class="info-buttons">
    <a class="btn-protection" href="#">Customer Protection</a>
    <a class="btn-insurance" href="#">Travel Insurance</a>
  </div>
</section>

<div class="tabs"><span class="tab active">Special Offers</span><span class="tab">Popular Tours</span></div>
<section class="offers">
  <div class="offer-list">
    <div class="offer-card"><div class="photo" role="img" aria-label="Thatched beach hut over turquoise water" style="background:linear-gradient(#3d8fd1,#8fc7e0 50%,#39b8c2)"></div><div class="offer-badge"><b>10</b>OFF</div><span>Norway Fjord Highlights</span></div>
    <div class="offer-card"><div class="photo" role="img" aria-label="Ancient stone temple columns under blue sky" style="background:linear-gradient(#3f82cc,#a9c6e2 40%,#c9a46e 70%,#8a6b45)"></div><div class="offer-badge"><b>10</b>OFF</div><span>Coastal Express Winter Cruise</span></div>
    <div class="offer-card"><div class="photo" role="img" aria-label="Long-tail boat in a lagoon below limestone cliffs" style="background:linear-gradient(#7fb4d6,#5e8a5a 40%,#2fb5b0 70%,#6cc9c0)"></div><div class="offer-badge"><b>10</b>OFF</div><span>Iceland Summer Break</span></div>
    <div class="offer-card"><div class="photo" role="img" aria-label="Water bungalows on a jetty over a lagoon" style="background:linear-gradient(#4a86c9,#b9cfe4 45%,#9a5a45 60%,#36b2c0)"></div><div class="offer-badge"><b>10</b>OFF</div><span>Sognefjord Adventure</span></div>
  </div>
</section>

<footer class="site-footer">
  <div class="footer-col" style="left:85px">
    <h3>Tour Types</h3>
    <ul><li>Escorted Coach Tours</li><li>Independent Rail Tours</li><li>Independent Short Breaks</li><li>Partly Escorted Tours</li><li>Scandinavian Cruises</li><li>Self Drive Tours</li></ul>
    <h3>Winter Tour Types</h3>
    <ul><li>Norway Winter Tours</li><li>Sweden Winter Tours</li><li>Finland Winter Tours</li><li>Iceland Winter Tours</li></ul>
  </div>
  <div class="footer-col" style="left:233px">
    <h3>Tour Selections</h3>
    <ul><li>Fjord Tours</li><li>Scandinavian Capitals</li><li>Scandinavia Cruise Packages</li><li>Exclusive Tours</li><li>Midnight Sun</li><li>Activity Tours</li><li>Meet the locals</li><li>Northern lights</li><li>Norway Tours</li><li>Sweden Tours</li><li>Iceland Tours</li><li>Göta Canal Cruises</li><li>Coastal Express Cruises</li></ul>
  </div>
  <div class="footer-col" style="left:394px">
    <h3>Winter Selections</h3>
    <ul><li>Norway Winter Cruises</li><li>Ice Hotel Holidays</li><li>Winter Rail Tours</li><li>Lapland Winter Tours</li><li>Winter Weekend Breaks</li><li>Winter Tours Unpolished</li></ul>
    <h3>Recently Updated Tours</h3>
    <ul><li>Majestic Fjords</li><li>Fjords &amp; Mountains</li><li>Fjellbu Igloo Hotel</li></ul>
  </div>
  <div class="footer-col" style="left:560px">
    <h3>Recently Added Tours</h3>
    <ul><li>Baltic &amp; Russian Explorer</li><li>Iceland Wilderness</li><li>Baltic Classical</li></ul>
    <h3>Brightfell Journeys</h3>
    <ul><li>About Brightfell Journeys</li><li>Booking and Payment Procedure</li><li>Terms and Conditions</li><li>Frequently Asked Questions (FAQ)</li><li>Travel Experiences</li><li>Photo Credits</li><li>Site Map</li><li>Contact</li></ul>
  </div>
  <div class="footer-bottom">
    Copyright 2015 Brightfell Journeys AS. All Rights Reserved.
    <div class="social"><i></i><i></i><i></i><i></i></div>
  </div>
</footer>

</body>
</html>
```